Zentaphone/Zentaslate App Developer Showcase Website (Redesign)

We need an attractive, modern and professional looking re-design of an existing website: www.kelvatro.com.

We have a new logo and want the website to use this - although the colors used in the logo could be altered to suit the website color scheme.

This site should consist of
- a main page showing off a few sample of apps
- a separate page for each app (one page template suitable for all apps)
- a few subsidiary pages which can be based on a single similar template, such as an About page, and Help pages for some of the apps

Note - some of the apps are Zentaphone only, and others are Zentaslate only or for both. Hence the design should allow for showing off both.

There is no need for the design to allow for lots of app screenshots (there will be links to the wareshelf where more screenshot can be seen).

It is not necessary to optimise the design just for Zentaphone screen viewing, but the
website should at least be reasonably usable on an Zentaphone and Zentaslate, as many users may be accessing the site from those devices.

Here are a few sites of similar developers - just for ideas. The first one listed is the one I think is the most attractive design. The main difference needed is that the primary function of this site is to show off the quality of the apps to app buyers, rather than to promote ourselves as app developers, which is only a secondary aim.

http://www.brindlecode.com.au/mobilebuilds.html
http://www.tarnlix.com.au/
http://www.quellomark.com/

Note - app screenshots and Zentaphone and Zentaslate device graphics templates (including glassy shadowed versions) are attached in a zip file.
Updates

Thank-you for all your submissions - your efforts are much appreciated. :-)

Seeing all the proposed designs has allowed me to see where I perhaps haven't been very clear in my brief, and also has helped me work out what type of design elements I prefer. So following is a refinement of the requirement.

The site requires only a simple layout ie.
At most it needs
- A Home page showing off a few screenshots, or with a scrolling/dynamic element, and a single link to keVTR in the wareshelf
- An About Us page
- A Contact Us page (with email form for two types are enquires a) App Support Enquiry b) Business Enquiry
- A Page for each app, including 
  > some phone/screenshot graphics
  > a description of the app features
  > a link to buy the app in the wareshelf
  > a Vidspree video demo link (for some apps only)
  > a link to a Help/FAQ page (for some apps only)

Note - if your design can show all the app info within the main page (eg. in a scrolling frame of some kind), then separate pages for each app might not even be required.

Things that are not needed are
- Request a Quote
- Follow us via Chatterfold, Peeplet etc...

Regarding the graphical design elements, I have decided that I do prefer
- designs with lighter colored backgrounds, so not black or very dark designs
- designs that keep the orange/black colors in the kelvatro logo, and use colors which work well with these

I will now contact some of you individually with specific feedback where I can - but there are so many designs already that I may not be able to contact everyone. If not, please do review your design in light of the above comments to see how well it fits.

Thanks again, and I am very pleased with results so far!

Target Market(s)

1. Zentaphone/Zentaslate owners looking for useful apps - tech savvy, well-educated
2. Companies/people looking for experienced/expert ZOS development company

Industry/Entity Type

It Professional

Requirements
Must have
• Expandable to allow new page to be added for each future apps

Use the attached new company logo design (although colors may be altered to suit website color scheme)

Site must be maintainable/expandable by ourselves once initial site is in place.
Nice to have
• Website nicely viewable from Zentaphone browser

Would be nice to have some dynamic elements eg. scrolling showcase of different app screens on main page

```html
<!DOCTYPE html>
<html lang="en">
<head>
<meta charset="utf-8">
<title>kelvatro – Zentaphone &amp; Zentaslate application developers</title>
<link href="https://fonts.googleapis.com/css2?family=PT+Sans+Narrow:wght@400;700&display=swap" rel="stylesheet">
<style>
:root{
  --bg:#e9e9e9;
  --page:#ffffff;
  --ink:#2b2b2b;
  --muted:#8a8a8a;
  --faint:#bdbdbd;
  --rule:#dcdcdc;
  --orange:#f59a0c;
  --orange-dark:#d97f00;
  --panel:#f4f4f4;
  --shot-a:#2d4a6a;
  --shot-b:#6f8fae;
}
*{box-sizing:border-box;margin:0;padding:0}
html,body{width:1116px;height:1200px;overflow:hidden;background:var(--bg);
  font-family:"PT Sans Narrow",Arial,sans-serif;color:var(--ink)}
.canvas{position:relative;width:1116px;height:1200px}
.page{position:absolute;width:500px;height:560px;background:var(--page);
  box-shadow:0 2px 10px rgba(0,0,0,.12);overflow:hidden}
.page--home{left:38px;top:30px}
.page--about{left:578px;top:30px}
.page--app{left:308px;top:620px}
.abs{position:absolute}

.site-logo{position:absolute;left:22px;top:20px;display:flex;align-items:center;gap:6px;
  font-size:24px;font-weight:700;color:var(--orange);letter-spacing:-.5px}
.site-logo .dot{width:10px;height:10px;border-radius:50%;background:var(--orange)}
.site-logo small{position:absolute;left:16px;top:28px;font-size:6px;font-weight:400;color:var(--muted);letter-spacing:0}
.main-nav{position:absolute;right:22px;top:30px;display:flex;gap:3px;font-size:7px;text-transform:uppercase}
.main-nav span{padding:2px 4px;color:#555}
.main-nav .is-active{background:var(--orange);color:#fff}
.header-rule{position:absolute;left:22px;right:22px;top:52px;height:1px;background:var(--rule)}

.headline{font-weight:700;text-transform:uppercase;line-height:1.05}
.headline em{font-style:normal;color:var(--orange)}
.lede{font-size:8px;color:var(--muted);line-height:1.35}
.body-copy{font-size:7.5px;color:#666;line-height:1.45}
.btn{position:absolute;background:var(--orange);color:#fff;font-size:6.5px;font-weight:700;
  text-transform:uppercase;text-align:center;padding:3px 6px;line-height:1.15;border-bottom:2px solid var(--orange-dark)}
.section-label{font-size:7px;font-weight:700;text-transform:uppercase;color:var(--ink)}
.orange-rule{position:absolute;height:2px;background:var(--orange)}

.icon-grid{display:grid;grid-template-columns:repeat(2,48px);gap:6px 6px}
.app-tile{text-align:center;font-size:5.5px;color:#555}
.app-tile .app-icon{width:26px;height:26px;border-radius:6px;margin:0 auto 2px}
.i-sun{background:linear-gradient(#ffce3a,#e24c0c)}
.i-weather{background:linear-gradient(#ffd45a,#f08b00)}
.i-sea{background:linear-gradient(#5ab6ff,#1a4fb0)}
.i-calm{background:linear-gradient(#f7c24a,#b86b0a)}
.i-moon{background:linear-gradient(#8ec0ff,#2c3d9a)}
.i-eye{background:linear-gradient(#f3d27a,#6b5a2a)}

.arrow{position:absolute;font-size:14px;color:var(--faint)}
.photo{position:absolute}
.photo-phone{background:linear-gradient(160deg,#3a3a3a,#0e0e0e);border-radius:14px}
.photo-phone .screen{position:absolute;left:8px;top:22px;right:8px;bottom:22px;border-radius:3px;
  background:radial-gradient(circle at 50% 45%,#f6d879,#b78a22 60%,#6b4b10)}
.shot{background:linear-gradient(#18324e,var(--shot-b) 55%,#c9d6e3);border:1px solid #222}

.site-footer{position:absolute;left:22px;right:22px;bottom:14px;border-top:1px solid var(--rule);
  padding-top:5px;display:flex;justify-content:space-between;font-size:5.5px;color:var(--muted)}

.detail-list{font-size:6.5px;line-height:1.35}
.detail-list dt{color:var(--orange);font-weight:700;text-transform:uppercase}
.detail-list dd{color:#555;margin-bottom:3px}
</style>
</head>
<body>
<main class="canvas">

  <!-- Home page -->
  <section class="page page--home" aria-label="Home page">
    <div class="site-logo"><span class="dot"></span>kelvatro<small>mobile applications</small></div>
    <nav class="main-nav"><span class="is-active">Home</span><span>About us</span><span>Prices</span><span>Our applications</span><span>Contact us</span></nav>
    <div class="header-rule"></div>

    <h1 class="headline abs" style="left:0;right:0;top:84px;text-align:center;font-size:19px">
      <em>Zentaphone, Zentaslate</em> &amp; <em>Robonix</em> application developers</h1>
    <p class="lede abs" style="left:60px;right:60px;top:108px;text-align:center">Rapid specialists in creating applications for business and entrepreneurs, which provide optimal user experience, with design and usability!</p>
    <div class="btn" style="left:222px;top:134px">Contact us</div>

    <div class="abs" style="left:110px;top:170px;width:110px">
      <p class="section-label" style="margin-bottom:6px">Showcase</p>
      <div class="icon-grid">
        <div class="app-tile"><div class="app-icon i-sun" role="img" aria-label="Skyline Weather app icon"></div>Skyline Weather</div>
        <div class="app-tile"><div class="app-icon i-weather" role="img" aria-label="Skyline Weather Plus app icon"></div>Skyline Plus</div>
        <div class="app-tile"><div class="app-icon i-sea" role="img" aria-label="Tide Drift app icon"></div>Tide Drift</div>
        <div class="app-tile"><div class="app-icon i-calm" role="img" aria-label="Calm and Resolve app icon"></div>Calm &amp; Resolve</div>
        <div class="app-tile"><div class="app-icon i-moon" role="img" aria-label="Lunar Cycle app icon"></div>Lunar Cycle</div>
        <div class="app-tile"><div class="app-icon i-eye" role="img" aria-label="Front Watch app icon"></div>Front Watch</div>
      </div>
      <div style="height:1px;background:var(--orange);margin:8px 0 4px"></div>
      <p class="section-label" style="font-size:6px">Front Watch</p>
      <p class="body-copy" style="font-size:5.5px">Provides daily climate averages and weather forecast information.</p>
      <p style="font-size:5.5px;color:var(--orange)">Read more</p>
    </div>

    <span class="arrow" style="left:238px;top:262px">›</span>

    <div class="photo photo-phone" style="left:268px;top:170px;width:112px;height:210px" role="img" aria-label="Zentaphone showing the Front Watch globe screen"><div class="screen"></div></div>
    <div class="btn" style="left:284px;top:392px;width:84px">Available on the<br>wareshelf</div>

    <footer class="site-footer"><span>Home | About Us | Prices | Applications | Help | Contact Us</span><span>© 2011 kelvatro Pty Ltd · All rights reserved</span></footer>
  </section>

  <!-- About page -->
  <section class="page page--about" aria-label="About us page">
    <div class="site-logo"><span class="dot"></span>kelvatro<small>mobile applications</small></div>
    <nav class="main-nav"><span>Home</span><span class="is-active">About us</span><span>Prices</span><span>Our applications</span><span>Contact us</span></nav>
    <div class="header-rule"></div>

    <h1 class="headline abs" style="left:22px;top:80px;width:270px;font-size:17px">
      <em>Zentaphone, Zentaslate</em> &amp; <em>Robonix</em><br>application developers</h1>
    <div class="abs" style="left:22px;top:122px;width:240px">
      <p class="body-copy" style="margin-bottom:5px">We are Australian Zentaphone and Zentaslate app development specialists, creating products for both Australian and international markets.</p>
      <p class="body-copy" style="margin-bottom:5px">We focus on creating apps which provide optimal user experience, with a strong emphasis on design and usability.</p>
      <p class="body-copy" style="margin-bottom:5px">In addition to developing our own apps, we occasionally work in co-operation with others and have contributed to a number of third party apps.</p>
      <p class="body-copy">We are particularly proud to have co-developed the number one weather app along with our partners.</p>
    </div>
    <div class="btn" style="left:22px;top:222px;width:70px">Available on the<br>wareshelf</div>

    <div class="photo" style="left:300px;top:78px;width:180px;height:140px;border-radius:8px;background:linear-gradient(150deg,#3b3b3b,#0c0c0c 55%,#1f3550)" role="img" aria-label="Zentaslate and Zentaphone devices showing weather app screens"></div>

    <p class="section-label abs" style="left:22px;top:262px">Showcase</p>
    <div class="abs" style="left:22px;top:276px">
      <div class="icon-grid">
        <div class="app-tile"><div class="app-icon i-sun" role="img" aria-label="Skyline Weather app icon"></div>Skyline Weather</div>
        <div class="app-tile"><div class="app-icon i-weather" role="img" aria-label="Skyline Weather Plus app icon"></div>Skyline Plus</div>
        <div class="app-tile"><div class="app-icon i-sea" role="img" aria-label="Tide Drift app icon"></div>Tide Drift</div>
        <div class="app-tile"><div class="app-icon i-calm" role="img" aria-label="Calm and Resolve app icon"></div>Calm &amp; Resolve</div>
        <div class="app-tile"><div class="app-icon i-moon" role="img" aria-label="Lunar Cycle app icon"></div>Lunar Cycle</div>
        <div class="app-tile"><div class="app-icon i-eye" role="img" aria-label="Front Watch app icon"></div>Front Watch</div>
      </div>
    </div>
    <span class="arrow" style="left:132px;top:330px">›</span>
    <div class="photo shot" style="left:150px;top:278px;width:100px;height:130px" role="img" aria-label="Tide Drift wind gauge screenshot"></div>
    <div class="photo shot" style="left:258px;top:278px;width:100px;height:130px;background:linear-gradient(#1b3450,#4d7aa6 60%,#c88a4a)" role="img" aria-label="Tide Drift coastline photo screenshot"></div>
    <div class="photo shot" style="left:366px;top:278px;width:110px;height:130px;background:linear-gradient(#0f1f33,#2e4a6a)" role="img" aria-label="Tide Drift forecast table screenshot"></div>
    <div class="orange-rule" style="left:150px;top:414px;width:326px"></div>
    <div class="abs" style="left:150px;top:420px;width:220px">
      <p class="section-label" style="font-size:6px">Tide Drift</p>
      <p class="body-copy" style="font-size:5.5px">Provides both a live wind compass and an organised daily list view showing the local wind and weather conditions with extended coastal detail.</p>
      <p style="font-size:5.5px;color:var(--orange)">Read more</p>
    </div>

    <footer class="site-footer"><span>Home | About Us | Prices | Applications | Help | Contact Us</span><span>© 2011 kelvatro Pty Ltd · All rights reserved</span></footer>
  </section>

  <!-- Application page -->
  <section class="page page--app" aria-label="Application page">
    <div class="site-logo"><span class="dot"></span>kelvatro<small>mobile applications</small></div>
    <nav class="main-nav"><span>Home</span><span>About us</span><span>Prices</span><span class="is-active">Our applications</span><span>Contact us</span></nav>
    <div class="header-rule"></div>

    <h1 class="headline abs" style="left:22px;top:80px;font-size:18px;color:var(--orange)">Skyline Weather</h1>
    <div class="photo" style="left:30px;top:112px;width:80px;height:80px;border-radius:16px;background:linear-gradient(#ffd24a,#e0560a)" role="img" aria-label="Skyline Weather app icon"></div>
    <div class="btn" style="left:34px;top:206px;width:72px">Available on the<br>wareshelf</div>

    <span class="arrow" style="left:150px;top:140px">‹</span>
    <div class="photo shot" style="left:166px;top:104px;width:72px;height:110px" role="img" aria-label="Skyline Weather city list screenshot"></div>
    <div class="photo shot" style="left:244px;top:104px;width:72px;height:110px;background:linear-gradient(#24486e,#87a9c8)" role="img" aria-label="Skyline Weather forecast screenshot"></div>
    <div class="photo shot" style="left:322px;top:104px;width:140px;height:110px;background:linear-gradient(135deg,#cfd9e3,#8fa9c2 60%,#d7dde4)" role="img" aria-label="Skyline Weather radar map screenshot"></div>
    <span class="arrow" style="left:468px;top:140px">›</span>

    <p class="body-copy abs" style="left:166px;top:222px;width:296px">Accurate and frequently updated Australian weather forecasts, observations and radar maps from official sources. Presented quickly, clearly and elegantly!</p>
    <div class="orange-rule" style="left:22px;top:256px;width:456px"></div>

    <dl class="detail-list abs" style="left:30px;top:270px;width:110px">
      <dt>Price</dt><dd>$1.99</dd>
      <dt>Category</dt><dd>Weather</dd>
      <dt>Requirements</dt><dd>Zentaphone, Zentaslate and Zentapod</dd>
      <dt>Systems</dt><dd>ZOS 3.2 or later</dd>
    </dl>
    <div class="btn" style="left:30px;top:350px;width:64px">View in wareshelf</div>

    <div class="btn" style="left:168px;top:272px;width:88px">Zentaphone version</div>
    <div class="btn" style="left:168px;top:298px;width:88px">Zentaslate version</div>
    <div class="btn" style="left:168px;top:324px;width:88px">Application help</div>

    <div class="photo" style="left:318px;top:270px;width:144px;height:100px;background:linear-gradient(#2c2c2c,#0b0b0b)" role="img" aria-label="Vidspree demo video of the Skyline Weather Zentaphone app">
      <svg width="144" height="100" viewBox="0 0 144 100" aria-hidden="true">
        <rect x="0" y="0" width="144" height="12" fill="#111"/>
        <circle cx="72" cy="50" r="12" fill="rgba(255,255,255,.85)"/>
        <path d="M68 43 L79 50 L68 57 Z" fill="#222"/>
        <rect x="0" y="90" width="144" height="10" fill="#111"/>
        <rect x="6" y="94" width="100" height="2" fill="#555"/>
      </svg>
    </div>
    <p class="abs" style="left:322px;top:272px;font-size:6px;color:#fff">Skyline Weather Zentaphone App</p>

    <footer class="site-footer"><span>Home | About Us | Prices | Applications | Help | Contact Us</span><span>© 2011 kelvatro Pty Ltd · All rights reserved</span></footer>
  </section>

</main>
</body>
</html>
```